Sunridge Lighting Distributors Business Card Design

Use logo and expand the framing box to the extents of the business card. Keep company name in right bottom corner and triangle at top right corner. I would like to have a template so that I can fill in employee name, contact info, email and website.

```html
<!DOCTYPE html>
<html lang="en">
<head>
<meta charset="utf-8">
<title>Sunridge Lighting Distributors – Business Card</title>
<link href="https://fonts.googleapis.com/css2?family=Bebas+Neue&display=swap" rel="stylesheet">
<style>
  :root {
    --backdrop: #3a3a3c;
    --card-navy: #12202b;
    --frame-white: #ffffff;
    --accent-blue: #0784c8;
    --bar: 10px;
  }
  * { margin: 0; padding: 0; box-sizing: border-box; }
  html, body { width: 1200px; height: 689px; overflow: hidden; background: var(--backdrop); }
  .sheet { position: relative; width: 1200px; height: 689px; }

  .card {
    position: absolute; top: 190px;
    width: 540px; height: 309px;
    background: var(--card-navy);
    overflow: hidden;
    font-family: "Bebas Neue", "Oswald", sans-serif;
    box-shadow: 0 14px 30px rgba(0,0,0,.35);
  }
  .card--front { left: 40px; }
  .card--back { left: 620px; }

  .frame-bar { position: absolute; background: var(--frame-white); }
  .frame-bar--top { top: 24px; left: 24px; width: 292px; height: var(--bar); }
  .frame-bar--right { top: 72px; right: 24px; width: var(--bar); height: 213px; }
  .frame-bar--bottom { bottom: 24px; right: 24px; height: var(--bar); }

  .corner-triangle { position: absolute; top: 0; left: 0; }

  /* front */
  .card--front .frame-bar--left { top: 24px; left: 24px; width: var(--bar); height: 80px; }
  .card--front .frame-bar--bottom { width: 140px; }
  .company-name {
    position: absolute; left: 28px; top: 122px;
    color: var(--frame-white);
    font-size: 58px; font-weight: 400; line-height: 0.92; letter-spacing: 1px;
    text-transform: uppercase;
  }

  /* back */
  .card--back .frame-bar--left { top: 24px; left: 24px; width: var(--bar); height: 112px; }
  .card--back .frame-bar--left-low { bottom: 24px; left: 24px; width: var(--bar); height: 52px; }
  .card--back .frame-bar--bottom { left: 24px; }
  .person {
    position: absolute; left: 30px; top: 154px;
    color: var(--accent-blue); text-transform: uppercase;
  }
  .person__name { font-size: 42px; line-height: 0.95; letter-spacing: 1px; }
  .person__role { font-size: 22px; line-height: 1; letter-spacing: 1px; }

  .contact {
    position: absolute; left: 318px; top: 112px;
    list-style: none; color: var(--accent-blue);
    font-size: 14px; line-height: 1.15; letter-spacing: .5px;
    text-transform: uppercase;
  }
  .contact li { display: flex; align-items: flex-start; gap: 7px; margin-bottom: 3px; }
  .contact svg { width: 10px; height: 10px; margin-top: 2px; flex: none; fill: var(--accent-blue); }
</style>
</head>
<body>
<main class="sheet">

  <section class="card card--front" aria-label="Business card front">
    <svg class="corner-triangle" width="540" height="309" aria-hidden="true">
      <polygon points="324,30 462,0 526,66" fill="var(--accent-blue)"/>
    </svg>
    <div class="frame-bar frame-bar--top"></div>
    <div class="frame-bar frame-bar--left"></div>
    <div class="frame-bar frame-bar--right"></div>
    <div class="frame-bar frame-bar--bottom"></div>
    <h1 class="company-name">Sunridge<br>Lighting<br>Distributors</h1>
  </section>

  <section class="card card--back" aria-label="Business card back">
    <svg class="corner-triangle" width="540" height="309" aria-hidden="true">
      <polygon points="324,30 462,0 526,66" fill="var(--accent-blue)"/>
    </svg>
    <div class="frame-bar frame-bar--top"></div>
    <div class="frame-bar frame-bar--left"></div>
    <div class="frame-bar frame-bar--left-low"></div>
    <div class="frame-bar frame-bar--right"></div>
    <div class="frame-bar frame-bar--bottom"></div>

    <div class="person">
      <p class="person__name">Daniel Reyes</p>
      <p class="person__role">Founder &amp; CEO</p>
    </div>

    <ul class="contact">
      <li>
        <svg viewBox="0 0 10 10" aria-hidden="true"><path d="M5 0a3.5 3.5 0 0 0-3.5 3.5C1.5 6 5 10 5 10s3.5-4 3.5-6.5A3.5 3.5 0 0 0 5 0zm0 5a1.4 1.4 0 1 1 0-2.8A1.4 1.4 0 0 1 5 5z"/></svg>
        <span>Your Address, City<br>State, Country, Zip 1235</span>
      </li>
      <li>
        <svg viewBox="0 0 10 10" aria-hidden="true"><path d="M2 0l2 2.2-1 1.2a6 6 0 0 0 3.6 3.6l1.2-1L10 8l-1.2 1.6C4.5 10 0 5.5.4 1.2z"/></svg>
        <span>(123) 456-7890</span>
      </li>
      <li>
        <svg viewBox="0 0 10 10" aria-hidden="true"><path d="M2.5 0h5v10h-5zM3.5 1v7h3V1z"/></svg>
        <span>(123) 456-7890</span>
      </li>
      <li>
        <svg viewBox="0 0 10 10" aria-hidden="true"><path d="M0 2h10v6H0zm1 1v.3l4 2.5 4-2.5V3z"/></svg>
        <span>daniel@yourwebsite.com</span>
      </li>
      <li>
        <svg viewBox="0 0 10 10" aria-hidden="true"><path d="M5 0a5 5 0 1 0 0 10A5 5 0 0 0 5 0zm0 1a4 4 0 0 1 0 8V1zM1.2 4.5h7.6v1H1.2z"/></svg>
        <span>www.yourwebsite.com</span>
      </li>
    </ul>
  </section>

</main>
</body>
</html>
```